The name of my company is Tolmen Refacing LLC and I would like the sub text to say "Cabinet Refacing and Countertops". Have my name Dorian Tolmen, Owner / Sales, contact info: Cell: 360-555-0147 / Email: dorian.tolmen@quenmail.com

Simple, Clean, and Organized. With colors that will appeal to the eye.

Target Market(s)

Houses and Apartments

Industry/Entity Type

Cabinet Refacing

Contact Information for Business Card

Company name and sub text Dorian Tolmen - Owner / Sales, my cell phone number and email

Requirements
Must have
• Business name, my name / position, and my contact info
Nice to have
• Simple. Organized. Appealing to the eye

```html
<!DOCTYPE html>
<html lang="en">
<head>
<meta charset="utf-8">
<title>Tolmen Refacing LLC – Business Card</title>
<link rel="stylesheet" href="https://fonts.googleapis.com/css2?family=Montserrat:wght@300;400;600;700&display=swap">
<style>
  :root {
    --brand-blue: #4269b2;
    --card-white: #ffffff;
    --ink-dark: #1f2430;
    --ink-grey: #a9b0bc;
    --arc-grey: #c4c4c4;
    --page-bg: #e6e7ea;
  }
  html, body {
    margin: 0;
    padding: 0;
    width: 1200px;
    height: 1186px;
    overflow: hidden;
    background: var(--page-bg);
    font-family: "Montserrat", sans-serif;
  }
  .canvas {
    position: relative;
    width: 1200px;
    height: 1186px;
  }
  .card {
    position: absolute;
    left: 140px;
    width: 920px;
    height: 526px;
    border-radius: 34px;
    overflow: hidden;
    box-shadow: 0 10px 30px rgba(0,0,0,0.18);
  }
  .card--back { top: 44px; background: var(--brand-blue); }
  .card--front { top: 616px; background: var(--card-white); }
  .card svg { display: block; }

  .brand-name { font-weight: 300; letter-spacing: 1px; }
  .brand-tagline { font-weight: 400; letter-spacing: 2px; }
  .person-name { font-weight: 700; }
  .person-role { font-weight: 300; }
  .contact-line { font-weight: 400; }
</style>
</head>
<body>
<main class="canvas">

  <!-- Back of card: brand side -->
  <section class="card card--back" aria-label="Card back with company name">
    <svg width="920" height="526" viewBox="0 0 920 526">
      <rect class="brand-mark" x="408" y="120" width="104" height="104" fill="#ffffff"/>
      <text class="brand-name" x="460" y="320" text-anchor="middle" font-size="58" fill="#ffffff">TOLMEN REFACING, LLC</text>
      <text class="brand-tagline" x="460" y="372" text-anchor="middle" font-size="24" fill="#ffffff">CABINET REFACING AND COUNTERTOPS</text>
    </svg>
  </section>

  <!-- Front of card: contact side -->
  <section class="card card--front" aria-label="Card front with contact details">
    <svg width="920" height="526" viewBox="0 0 920 526">
      <path class="wave-arc" d="M540 300 C720 292 840 210 920 96" fill="none" stroke="var(--arc-grey)" stroke-width="16"/>
      <path class="wave-band" d="M0 526 V480 C110 330 300 300 480 300 C660 300 800 230 920 126 V526 Z" fill="var(--brand-blue)"/>

      <rect class="brand-mark" x="60" y="60" width="70" height="70" fill="var(--brand-blue)"/>
      <text class="brand-name" x="60" y="184" font-size="40" fill="var(--ink-grey)">TOLMEN REFACING, LLC</text>
      <text class="brand-tagline" x="62" y="214" font-size="15" font-weight="600" fill="var(--ink-dark)">CABINET REFACING AND COUNTERTOPS</text>

      <text class="person-name" x="220" y="400" font-size="30" fill="#ffffff">Dorian Tolmen</text>
      <text class="person-role" x="222" y="428" font-size="18" fill="#ffffff">Owner / Sales</text>

      <g class="contact-phone" fill="#ffffff">
        <path d="M226 452 c2-2 5-2 6 0 l2 4 c1 2 0 3-1 4 l-1 1 c1 3 3 5 6 6 l1-1 c1-1 2-2 4-1 l4 2 c2 1 2 4 0 6 c-3 3-8 3-13-1 c-5-4-9-9-9-14 c0-3 0-5 1-6z"/>
        <text class="contact-line" x="254" y="468" font-size="18">360-555-0147</text>
      </g>
      <g class="contact-email" fill="#ffffff">
        <rect x="226" y="484" width="20" height="14" rx="2"/>
        <path d="M227 485 L236 493 L245 485" fill="none" stroke="var(--brand-blue)" stroke-width="2"/>
        <text class="contact-line" x="254" y="498" font-size="18">dorian.tolmen@quenmail.com</text>
      </g>
    </svg>
  </section>

</main>
</body>
</html>
```